Vrano = Difficult

Sto Je Treba Ni Vrano
what must be done, is not difficult...

my mom is Croatian and her name is Ranka.

a Croatian expression that I came across 12 years ago is 'what must be done, is not difficult'. yes, it is counter-intuitive. but it helped me to get divorced and then to beat Stage 4 cancer. both seem impossible,

but they they had to be done, so they were not difficult.

so I have started up a new company called:
Vrano Consulting - solving difficult

I'll be working with companies that have a difficult program/project that they haven't launched yet...

I envision possibly a business card that is shaped into a "D" to represent the Croatian word of difficult.

yes, I know this is difficult - welcome to my new world - the difficult challenges are worth solving...

a nod to the red/white design of the Croatian flag would be nice.

```html
<!DOCTYPE html>
<html lang="en">
<head>
<meta charset="utf-8">
<title>Vrano Consulting – Business Card</title>
<link rel="stylesheet" href="https://fonts.googleapis.com/css2?family=Exo+2:wght@400;600&display=swap">
<style>
  :root {
    --card-red: #ed1c24;
    --card-red-light: #f4777c;
    --paper: #ffffff;
    --ink-light: #ffffff;
  }
  html, body {
    margin: 0;
    padding: 0;
    width: 1000px;
    height: 1200px;
    overflow: hidden;
    background: var(--paper);
  }
  .stage {
    display: block;
    width: 1000px;
    height: 1200px;
  }
  .card-fill { fill: var(--card-red); }
  .frame-line { fill: none; stroke: var(--ink-light); stroke-width: 3; }
  .card-text {
    font-family: "Exo 2", "Segoe UI", sans-serif;
    fill: var(--ink-light);
  }
  .holder-name { font-size: 38px; font-weight: 600; }
  .contact-line { font-size: 28px; font-weight: 400; }
  .email-line { font-size: 23px; font-weight: 400; }
  .brand-name { font-size: 41px; font-weight: 400; }
  .tagline { font-size: 41px; font-weight: 400; }
</style>
</head>
<body>
<svg class="stage" viewBox="0 0 1000 1200" xmlns="http://www.w3.org/2000/svg">
  <defs>
    <filter id="card-shadow" x="-20%" y="-20%" width="140%" height="140%">
      <feDropShadow dx="-4" dy="8" stdDeviation="7" flood-color="#000" flood-opacity="0.35"/>
    </filter>
    <linearGradient id="flag-pattern-tone" x1="0" y1="0" x2="1" y2="1">
      <stop offset="0" stop-color="var(--card-red)"/>
      <stop offset="0.5" stop-color="var(--card-red-light)"/>
      <stop offset="1" stop-color="var(--card-red)"/>
    </linearGradient>
  </defs>

  <!-- Contact side -->
  <g class="card card-contact">
    <path class="card-fill" filter="url(#card-shadow)"
      d="M130 44 H489 V802 H130 Q40 802 40 712 V134 Q40 44 130 44 Z"/>
    <path class="frame-line"
      d="M136 69 H464 V777 H136 Q66 777 66 707 V139 Q66 69 136 69 Z"/>
    <text class="card-text holder-name" x="397" y="383" text-anchor="end">Dane Holt</text>
    <text class="card-text contact-line" x="397" y="510" text-anchor="end">218 Linden Avenue</text>
    <text class="card-text contact-line" x="397" y="548" text-anchor="end">Marlow, GA 30412</text>
    <text class="card-text contact-line" x="397" y="585" text-anchor="end">404-555-0193</text>
    <text class="card-text email-line" x="261" y="718" text-anchor="middle">dane@vranoconsulting.com</text>
  </g>

  <!-- Brand side -->
  <g class="card card-brand">
    <path role="img" aria-label="Red and white checkered border pattern inspired by the Croatian flag"
      fill="url(#flag-pattern-tone)" filter="url(#card-shadow)"
      d="M509 334 H882 Q957 334 957 409 V1018 Q957 1093 882 1093 H509 Z"/>
    <path class="card-fill"
      d="M583 467 H822 Q882 467 882 527 V906 Q882 966 822 966 H583 Z"/>
    <path class="frame-line"
      d="M595 484 H798 Q868 484 868 554 V883 Q868 953 798 953 H595 Z"/>
    <text class="card-text brand-name" x="613" y="638">Vrano</text>
    <text class="card-text brand-name" x="613" y="690">Consulting</text>
    <text class="card-text tagline" x="850" y="758" text-anchor="end">- solving</text>
    <text class="card-text tagline" x="850" y="808" text-anchor="end">difficult</text>
  </g>
</svg>
</body>
</html>
```